Plumbing business card and logo desgin

Need a new business card and logo for a plumbing business based in Warragul, Australia. Business name is 9Brook plumbing & air-conditioning. We service all plumbing and gasfitting needs and installation of air-conditioning. We clear blocked drains, install new hot water systems, central heating, new and existing homes, roofing, sanitary and drainage.
i would like to have a space on there for website, email, phone, licence number and what we do as a company.
i would like a water droplet to be incorporated into the design to try and stand out that we are a plumbing business

Contact Information for Business Card

phone number: 0497215836
Licence Number: 873614

Logo Text

9Brook Plumbing & Air-Conditioning

```html
<!DOCTYPE html>
<html lang="en">
<head>
<meta charset="utf-8">
<title>9Brook Plumbing &amp; Air-Conditioning – Business Card</title>
<link rel="stylesheet" href="https://fonts.googleapis.com/css2?family=Montserrat:wght@700;800&family=Poppins:wght@400;600;700&display=swap">
<style>
  :root {
    --page-bg: #1c1c1e;
    --card-bg: #3a3a3d;
    --card-bg-light: #47474b;
    --blue: #1a8fe0;
    --blue-deep: #0a6fc2;
    --white: #ffffff;
    --pale: #e6f3fc;
  }
  * { margin: 0; padding: 0; box-sizing: border-box; }
  html, body { width: 1200px; height: 900px; overflow: hidden; background: var(--page-bg); }
  body { position: relative; font-family: "Poppins", sans-serif; color: var(--white); }

  .card {
    position: absolute;
    left: 250px;
    width: 700px;
    height: 400px;
    border-radius: 4px;
    overflow: hidden;
    box-shadow: 0 12px 30px rgba(0,0,0,.55);
  }
  .card--back { top: 40px; }
  .card--front { top: 460px; }

  .card__texture {
    position: absolute; inset: 0;
    background:
      radial-gradient(circle at 20% 30%, rgba(255,255,255,.05) 0 14px, transparent 15px),
      radial-gradient(circle at 70% 80%, rgba(255,255,255,.05) 0 20px, transparent 21px),
      radial-gradient(circle at 45% 15%, rgba(255,255,255,.04) 0 10px, transparent 11px),
      radial-gradient(circle at 30% 40%, var(--card-bg-light), var(--card-bg) 70%);
  }

  /* back */
  .mark-spot {
    position: absolute; left: 60px; top: 100px;
    width: 200px; height: 200px; border-radius: 50%;
    background: linear-gradient(135deg, var(--pale), var(--blue) 60%, var(--blue-deep));
  }
  .services {
    position: absolute; left: 310px; top: 62px;
    list-style: none;
    display: flex; flex-direction: column; gap: 10px;
  }
  .services__item {
    background: var(--blue);
    border-radius: 20px;
    padding: 6px 22px 5px 18px;
    font-family: "Montserrat", sans-serif;
    font-weight: 800;
    font-size: 19px;
    letter-spacing: .5px;
    text-transform: uppercase;
    width: max-content;
    min-width: 300px;
  }

  /* front */
  .feature-art {
    position: absolute;
    right: -90px; top: -40px;
    width: 380px; height: 380px;
    border-radius: 50%;
    background: radial-gradient(circle at 35% 35%, var(--pale) 0%, var(--blue) 45%, var(--blue-deep) 80%);
    opacity: .95;
  }
  .brand {
    position: absolute; left: 40px; top: 40px;
    display: flex; align-items: center; gap: 14px;
  }
  .brand__dot {
    width: 70px; height: 70px; border-radius: 50%;
    background: var(--blue);
    flex: none;
  }
  .brand__name {
    font-family: "Poppins", sans-serif;
    font-weight: 700;
    font-size: 28px;
    line-height: 1.1;
    color: var(--blue);
    width: 290px;
  }
  .contact {
    position: absolute; left: 40px; top: 170px;
    list-style: none;
    display: flex; flex-direction: column; gap: 10px;
  }
  .contact__row { display: flex; align-items: center; gap: 12px; font-size: 16px; }
  .contact__row--phone .contact__text {
    font-family: "Montserrat", sans-serif; font-weight: 800; font-size: 32px; letter-spacing: 1px;
  }
  .contact__icon {
    width: 30px; height: 30px; border-radius: 50%;
    background: var(--blue);
    display: flex; align-items: center; justify-content: center;
    flex: none;
  }
  .licence {
    position: absolute; left: 40px; top: 330px;
    background: var(--blue);
    border-radius: 22px;
    padding: 7px 22px;
    font-family: "Poppins", sans-serif;
    font-weight: 700;
    font-size: 19px;
  }
</style>
</head>
<body>

<section class="card card--back" aria-label="Business card back">
  <div class="card__texture" role="img" aria-label="Water droplet texture on dark grey"></div>
  <div class="mark-spot" role="img" aria-label="Brand mark area"></div>
  <ul class="services">
    <li class="services__item">Plumbing and gasfitting</li>
    <li class="services__item">Air-conditioning</li>
    <li class="services__item">Blocked drains</li>
    <li class="services__item">Hot water systems</li>
    <li class="services__item">Central heating</li>
    <li class="services__item">Roofing</li>
    <li class="services__item">Sanitary and drainage.</li>
  </ul>
</section>

<section class="card card--front" aria-label="Business card front">
  <div class="card__texture" role="img" aria-label="Water droplet texture on dark grey"></div>
  <div class="feature-art" role="img" aria-label="Large blue and white water brand decoration"></div>

  <div class="brand">
    <span class="brand__dot"></span>
    <span class="brand__name">9Brook Plumbing &amp; Air-Conditioning</span>
  </div>

  <ul class="contact">
    <li class="contact__row contact__row--phone">
      <span class="contact__icon">
        <svg width="16" height="16" viewBox="0 0 24 24" aria-hidden="true"><path fill="#fff" d="M6.6 10.8a15.1 15.1 0 0 0 6.6 6.6l2.2-2.2a1 1 0 0 1 1-.25 11.4 11.4 0 0 0 3.6.57 1 1 0 0 1 1 1V20a1 1 0 0 1-1 1A17 17 0 0 1 3 4a1 1 0 0 1 1-1h3.5a1 1 0 0 1 1 1c0 1.25.2 2.45.57 3.57a1 1 0 0 1-.25 1z"/></svg>
      </span>
      <span class="contact__text">0497215836</span>
    </li>
    <li class="contact__row">
      <span class="contact__icon">
        <svg width="16" height="16" viewBox="0 0 24 24" aria-hidden="true" fill="none" stroke="#fff" stroke-width="1.8"><circle cx="12" cy="12" r="9"/><ellipse cx="12" cy="12" rx="4" ry="9"/><path d="M3 12h18M5 7h14M5 17h14"/></svg>
      </span>
      <span class="contact__text">9Brookplumbing&amp;air-conditioning.com</span>
    </li>
    <li class="contact__row">
      <span class="contact__icon">
        <svg width="16" height="16" viewBox="0 0 24 24" aria-hidden="true" fill="none" stroke="#fff" stroke-width="1.8"><rect x="3" y="5" width="18" height="14" rx="1"/><path d="M3 6l9 7 9-7"/></svg>
      </span>
      <span class="contact__text">info@9Brookplumbing&amp;air-conditioning.com</span>
    </li>
  </ul>

  <div class="licence">Licence Number: 873614</div>
</section>

</body>
</html>
```